design an app for runners to engage them in Pacebound

Creative Brief: Running Application - Pacebound
Objective
To design a simple yet impactful mobile application for runners, centered around Pacebound. The app should offer an engaging, user-friendly experience while encouraging participation in running challenges. Starting with a minimalist and robust version, the design must focus on essential features, allowing for future enhancements as the user base grows.

Target Audience
Primary Users: Casual to dedicated runners who enjoy tracking their progress and participating in challenges.
Motivations: Community-driven goals, personal achievements, and tangible rewards.
Needs: A visually appealing, straightforward interface with real-time progress tracking and clear challenge objectives.
Core Features
Main Screen: Current Challenge

Displays the active challenge with a title, visual, prize description, and countdown for kilometers remaining.
Prominent “Join” button for easy participation.
Quick access to challenge conditions (eg, most kilometers, fastest pace, random draw).
Challenge Details

Includes challenge rules, detailed prize information, and victory conditions.
Simplified text for clarity and engagement.
Past Challenges

Showcases previous challenges, total kilometers achieved, and winners.
Admin Section

Enables challenge creation with scheduling, descriptions, and victory criteria.
Minimalist design for ease of use.
Look and Feel
Visual Identity: Clean, modern, and energetic design reflecting the spirit of running and collective achievement.
Color Palette:
Vibrant primary colors: Blue and green for energy and motivation.
Accent colors: Orange or yellow for highlights, paired with a dark background for strong contrast.
Typography:
Sans-serif fonts like Lato or Montserrat for readability.
Bold, prominent numbers for key statistics like kilometers completed.
Icons and Graphics:
Minimalistic icons with light, functional animations (eg, a moving kilometer counter).
Clear, motivational visuals to support collective progress.
Tone and Style
Tone: Encouraging, community-focused, and goal-oriented.
Style: Minimalistic with a focus on clarity and user engagement.
References
Inspirations:
Velta Stride Circle for its simplicity and modern interface.
Quorvo for its community features and tracking precision.
Deliverables
Wireframes and UI designs for all key screens: login, current challenge, challenge details, past challenges, and admin panel.
Visual assets: icons, buttons, and animations.
A consistent design system to ensure scalability for future features.
Updates

Target Market(s)

Casual to dedicated runners who enjoy tracking their progress and participating in challenges.

Industry/Entity Type

sport

Font styles to use
Sans Serif

Colors

Designer to choose colors to be used in the design.

Requirements
Must have
• to design all screens

```html
<!DOCTYPE html>
<html lang="en">
<head>
<meta charset="utf-8">
<title>Pacebound – App Screens</title>
<link rel="stylesheet" href="https://fonts.googleapis.com/css2?family=Montserrat:wght@600;700;800&family=Open+Sans:wght@400;600;700&display=swap">
<style>
  :root{
    --canvas:#e2e2e2;
    --screen:#363636;
    --field:#4a4a4a;
    --panel:#474747;
    --orange:#f98a1e;
    --orange-red:#f26a3a;
    --yellow:#f6b43a;
    --ink:#ffffff;
    --muted:#b9b9b9;
    --faint:#9a9a9a;
    --grid:#6a6a6a;
    --tab:#050505;
    --btn-ink:#333333;
  }
  *{box-sizing:border-box;margin:0;padding:0}
  html,body{width:1200px;height:647px;overflow:hidden;background:var(--canvas)}
  body{position:relative;font-family:"Open Sans",sans-serif;color:var(--ink)}
  .screen{position:absolute;background:var(--screen);overflow:hidden}
  .screen > *{position:absolute}
  .status-time{left:25px;top:7px;font-size:8.5px;font-weight:600}
  .status-icons{right:12px;top:9px;width:38px;height:8px}
  .brand{left:0;right:0;text-align:center;font-family:"Open Sans",sans-serif;font-weight:700;color:var(--ink);line-height:1}
  .brand-small{top:34px;font-size:10px}
  .brand-large{top:72px;font-size:16px}
  .heading{font-family:"Montserrat",sans-serif;font-weight:700;font-size:9px;letter-spacing:.6px}
  .lorem{font-size:5px;line-height:10.7px;color:var(--faint)}
  .field{background:var(--field);height:29px;font-size:7.5px;color:var(--muted);padding:0 8px;display:flex;align-items:center;justify-content:space-between}
  .btn{background:var(--orange);color:var(--btn-ink);font-size:9.5px;display:flex;align-items:center;justify-content:center;border-radius:2px}
  .tabbar{left:0;right:0;bottom:0;height:38px;background:var(--tab)}
  .tabbar svg{position:absolute;top:11px;width:15px;height:15px;color:#d8d8d8}
  .tabbar svg.active{color:var(--orange)}
  .tab-1{left:17px}.tab-2{left:71px}.tab-3{left:127px}.tab-4{left:181px}
  .icon{fill:none;stroke:currentColor;stroke-width:1.6;stroke-linecap:round;stroke-linejoin:round}

  .signup{left:114px;top:121px;width:216px;height:469px}
  .signin-line{left:0;right:0;top:408px;text-align:center;font-size:7.5px;color:var(--muted)}
  .signin-line b{color:var(--orange);font-weight:600}
  .home-indicator{left:74px;top:452px;width:72px;height:2px;border-radius:2px;background:#8a8a8a}

  .week{left:366px;top:121px;width:211px;height:457px}
  .day{top:102px;width:24px;text-align:center;font-size:6.5px;color:var(--muted)}
  .day-active{left:81px;top:81px;width:28px;height:38px;background:var(--orange);border-radius:2px;text-align:center;color:var(--btn-ink);font-weight:600}
  .day-active .num{display:block;font-size:10px;margin-top:8px}
  .day-active .lbl{display:block;font-size:6.5px}
  .metric-head{left:0;right:0;top:128px;display:flex;justify-content:center;align-items:center;gap:3px;font-size:8px;font-weight:600}
  .metric-head svg{width:9px;height:9px;color:var(--orange)}
  .stat{top:153px;width:44px;text-align:center;line-height:1.2}
  .stat b{display:block;font-size:8.5px;color:var(--orange);font-weight:600}
  .stat small{display:block;font-size:6px;color:var(--ink)}
  .km-ring{left:8px;top:216px;width:70px;height:70px}
  .km-value{left:8px;top:240px;width:70px;text-align:center;font-size:13px;color:var(--orange);font-weight:600;line-height:1}
  .km-unit{left:8px;top:257px;width:70px;text-align:center;font-size:6px;color:#3b2a5c}
  .goals{left:9px;top:308px;width:193px;height:59px;background:var(--field);border-radius:4px}
  .goals > *{position:absolute}
  .goals-title{left:10px;top:9px;font-size:7px;line-height:11px;width:80px}
  .goals-km{left:12px;top:34px;font-size:8px;font-weight:600}
  .goals-arrow{right:9px;top:7px;width:8px;height:8px;color:var(--muted)}
  .goal-dot{top:30px;width:10px;text-align:center;font-size:4.5px;color:var(--muted)}
  .goal-dot svg{display:block;width:10px;height:10px;margin-bottom:2px}

  .history{left:630px;top:121px;width:211px;height:469px}
  .chart{left:15px;top:73px;width:185px;height:132px;background:var(--panel)}
  .stats-card{left:13px;top:268px;width:185px;height:69px;background:var(--panel)}
  .stats-card > *{position:absolute}
  .sc-label{top:21px;font-size:5px;display:flex;align-items:center;gap:3px}
  .sc-label svg{width:7px;height:7px;color:var(--orange-red)}
  .sc-value{top:36px;font-size:6.5px}

  .profile{left:877px;top:127px;width:211px;height:457px}
  .person{left:13px;top:62px;font-size:7.5px;font-weight:600}
  .place{left:76px;top:63px;font-size:6px;color:var(--muted)}
  .avatar{left:161px;top:49px;width:42px;height:42px;border-radius:50%;background:radial-gradient(circle at 50% 45%,#c99a86,#7a4a3a 70%,#3a2a26)}
  .prize-box{left:19px;top:164px;width:54px;height:54px;background:var(--panel)}
  .prize-box svg{position:absolute;left:18px;top:9px;width:18px;height:14px;color:var(--yellow)}
  .prize-box span{position:absolute;left:0;right:0;top:32px;text-align:center;font-size:5px;color:var(--ink)}
  .win-card{left:13px;top:268px;width:185px;height:69px;background:var(--panel)}
  .win-card > *{position:absolute}
  .win-title{left:23px;top:10px;font-size:6.5px}
  .legend{left:24px;font-size:5px;display:flex;align-items:center;gap:6px}
  .legend i{display:inline-block;width:9px;height:2px;border-radius:1px}
  .mini-ring{width:26px;height:26px}
  .mini-ring span{position:absolute;left:0;right:0;top:9px;text-align:center;font-size:4.5px}
</style>
</head>
<body>
<svg width="0" height="0" style="position:absolute" aria-hidden="true">
  <symbol id="i-status" viewBox="0 0 38 8">
    <rect x="0" y="5" width="1.6" height="3" fill="#fff"/><rect x="2.6" y="3.6" width="1.6" height="4.4" fill="#fff"/><rect x="5.2" y="2" width="1.6" height="6" fill="#fff"/><rect x="7.8" y="0.5" width="1.6" height="7.5" fill="#fff"/>
    <path d="M13 3.2a6 6 0 0 1 8 0M14.5 5a3.6 3.6 0 0 1 5 0" fill="none" stroke="#fff" stroke-width="1.2" stroke-linecap="round"/><circle cx="17" cy="7" r="0.9" fill="#fff"/>
    <rect x="25" y="1" width="11" height="6" rx="1.5" fill="#fff"/><rect x="36.5" y="3" width="1" height="2" fill="#fff"/>
  </symbol>
  <symbol id="i-home" viewBox="0 0 24 24"><path class="icon" d="M3 11 12 3l9 8M5 9.5V21h5v-6h4v6h5V9.5"/></symbol>
  <symbol id="i-run" viewBox="0 0 24 24"><circle class="icon" cx="15" cy="4" r="2"/><path class="icon" d="M7 10l4-3 3 2 2 4 3 1M12 8l-2 6 4 3-1 5M10 14l-3 4H4"/></symbol>
  <symbol id="i-chart" viewBox="0 0 24 24"><path class="icon" d="M4 21V17M8 21v-6M12 21v-8M16 21v-10M20 21V7M3 14 9 8l4 3 7-7M16 4h4v4"/></symbol>
  <symbol id="i-user" viewBox="0 0 24 24"><circle class="icon" cx="12" cy="8" r="4"/><path class="icon" d="M4 21c0-4.4 3.6-7 8-7s8 2.6 8 7z"/></symbol>
  <symbol id="i-heart" viewBox="0 0 24 24"><path class="icon" d="M12 20S3 14.5 3 8.5A4.5 4.5 0 0 1 12 6a4.5 4.5 0 0 1 9 2.5C21 14.5 12 20 12 20z"/></symbol>
  <symbol id="i-clock" viewBox="0 0 24 24"><circle class="icon" cx="12" cy="12" r="9"/><path class="icon" d="M12 7v5l3 2"/></symbol>
  <symbol id="i-flame" viewBox="0 0 24 24"><path class="icon" d="M12 3c1 4 5 6 5 11a5 5 0 0 1-10 0c0-3 2-4 2-7 2 1 3 3 3 5"/></symbol>
  <symbol id="i-eye-off" viewBox="0 0 24 24"><path class="icon" d="M2 12s4-7 10-7 10 7 10 7-4 7-10 7S2 12 2 12z"/><circle class="icon" cx="12" cy="12" r="3"/><path class="icon" d="M4 20 20 4"/></symbol>
  <symbol id="i-chevron" viewBox="0 0 24 24"><path class="icon" d="M9 5l7 7-7 7"/></symbol>
  <symbol id="i-crown" viewBox="0 0 24 18"><path d="M2 4l5 6 5-8 5 8 5-6-2 10H4z" fill="currentColor"/><rect x="4" y="15" width="16" height="2.5" fill="currentColor"/></symbol>
  <symbol id="i-goal" viewBox="0 0 10 10"><circle cx="5" cy="5" r="3.8" fill="none" stroke="#3b2a5c" stroke-width="1.6"/><circle cx="5" cy="5" r="3.8" fill="none" stroke="#f98a1e" stroke-width="1.6" stroke-dasharray="18 6" transform="rotate(-90 5 5)"/></symbol>
</svg>

<section class="screen signup">
  <div class="status-time">9:41</div>
  <svg class="status-icons"><use href="#i-status"/></svg>
  <div class="brand brand-large">Pacebound</div>
  <div class="field" style="left:16px;top:160px;width:86px">First Name</div>
  <div class="field" style="left:114px;top:160px;width:86px">Last Name</div>
  <div class="field" style="left:16px;top:200px;width:184px">Email address</div>
  <div class="field" style="left:16px;top:240px;width:184px">Password <svg width="13" height="13" style="color:#c8c8c8"><use href="#i-eye-off"/></svg></div>
  <div class="field" style="left:16px;top:279px;width:184px">Address</div>
  <div class="field" style="left:16px;top:319px;width:97px">City</div>
  <div class="field" style="left:127px;top:319px;width:73px">Area Code</div>
  <div class="btn" style="left:16px;top:364px;width:184px;height:31px">Join Us</div>
  <div class="signin-line">Have an account? <b>Sign In</b></div>
  <div class="home-indicator"></div>
</section>

<section class="screen week">
  <div class="status-time">9:41</div>
  <svg class="status-icons"><use href="#i-status"/></svg>
  <div class="brand brand-small">Pacebound</div>
  <div class="heading" style="left:10px;top:58px">This Week’s</div>
  <div style="right:11px;top:60px;font-size:6.5px">See</div>
  <div class="day" style="left:1px">Mo</div>
  <div class="day" style="left:27px">Tu</div>
  <div class="day" style="left:55px">Wed</div>
  <div class="day-active"><span class="num">15</span><span class="lbl">Th</span></div>
  <div class="day" style="left:108px">Fr</div>
  <div class="day" style="left:134px">Sa</div>
  <div class="day" style="left:159px">Su</div>
  <div class="day" style="left:185px">Mo</div>
  <div class="metric-head"><svg><use href="#i-heart"/></svg>Cardio Points <svg><use href="#i-run"/></svg>Steps</div>
  <div class="stat" style="left:51px"><b>1.000</b><small>Calories</small></div>
  <div class="stat" style="left:88px"><b>3.83</b><small>Km</small></div>
  <div class="stat" style="left:124px"><b>70</b><small>Move Min</small></div>
  <p class="lorem" style="left:18px;top:180px;width:176px">Lorem ipsum dolor sit amet, consectetur adipiscing elit. Cras vitae, blandit tortor gravida pharetra nunc. Non turpis imperdiet viverra sed vulputate nisl scelerisque donec.</p>
  <svg class="km-ring" viewBox="0 0 70 70">
    <circle cx="35" cy="35" r="32" fill="none" stroke="#5a5a5a" stroke-width="4"/>
    <circle cx="35" cy="35" r="32" fill="none" stroke="#f98a1e" stroke-width="4" stroke-dasharray="180 21" transform="rotate(-70 35 35)"/>
  </svg>
  <div class="km-value">1264</div>
  <div class="km-unit">Km</div>
  <div class="btn" style="left:90px;top:225px;width:81px;height:24px;font-size:9.5px">Join Challenge</div>
  <p class="lorem" style="left:88px;top:258px;width:115px">Lorem ipsum dolor sit amet, consectetur adipiscing elit. Cras vitae, blandit tortor gravida pharetra nunc. Non turpis imperdiet viverra sed vulputate nisl scelerisque donec.</p>
  <div class="goals">
    <div class="goals-title">Your goals for Next Week</div>
    <svg class="goals-arrow"><use href="#i-chevron"/></svg>
    <div class="goals-km">5 Km</div>
    <div class="goal-dot" style="left:70px"><svg><use href="#i-goal"/></svg>S</div>
    <div class="goal-dot" style="left:87px"><svg><use href="#i-goal"/></svg>M</div>
    <div class="goal-dot" style="left:104px"><svg><use href="#i-goal"/></svg>T</div>
    <div class="goal-dot" style="left:121px"><svg><use href="#i-goal"/></svg>W</div>
    <div class="goal-dot" style="left:138px"><svg><use href="#i-goal"/></svg>T</div>
    <div class="goal-dot" style="left:155px"><svg><use href="#i-goal"/></svg>F</div>
    <div class="goal-dot" style="left:172px"><svg><use href="#i-goal"/></svg>S</div>
  </div>
  <div class="btn" style="left:13px;top:384px;width:184px;height:31px">Next&nbsp; Challenge</div>
  <nav class="tabbar">
    <svg class="tab-1"><use href="#i-home"/></svg>
    <svg class="tab-2 active"><use href="#i-run"/></svg>
    <svg class="tab-3"><use href="#i-chart"/></svg>
    <svg class="tab-4"><use href="#i-user"/></svg>
  </nav>
</section>

<section class="screen history">
  <div class="status-time">9:41</div>
  <svg class="status-icons"><use href="#i-status"/></svg>
  <div class="brand brand-small">Pacebound</div>
  <div class="heading" style="left:8px;top:58px">Last Week Challenge</div>
  <svg class="chart" viewBox="0 0 185 132" font-family="Open Sans, sans-serif" font-size="5" fill="#fff">
    <g stroke="#6a6a6a" stroke-width=".5">
      <line x1="26" y1="19" x2="173" y2="19"/><line x1="26" y1="35" x2="173" y2="35"/><line x1="26" y1="51" x2="173" y2="51"/>
      <line x1="26" y1="67" x2="173" y2="67"/><line x1="26" y1="83" x2="173" y2="83"/><line x1="26" y1="99" x2="173" y2="99"/>
    </g>
    <g text-anchor="end"><text x="20" y="21">1k</text><text x="20" y="37">500</text><text x="20" y="53">200</text><text x="20" y="69">100</text><text x="20" y="85">50</text><text x="20" y="101">0</text></g>
    <g stroke="#f26a3a" stroke-width="1.8" stroke-linecap="round">
      <line x1="28" y1="99" x2="28" y2="66"/><line x1="53" y1="99" x2="53" y2="35"/><line x1="74" y1="99" x2="74" y2="56"/>
      <line x1="98" y1="99" x2="98" y2="74"/><line x1="120" y1="99" x2="120" y2="25"/><line x1="143" y1="99" x2="143" y2="51"/><line x1="166" y1="99" x2="166" y2="46"/>
    </g>
    <g text-anchor="middle" font-size="6"><text x="28" y="115">Su</text><text x="53" y="115">Mo</text><text x="74" y="115">Tu</text><text x="98" y="115">We</text><text x="120" y="115">Th</text><text x="143" y="115">Fr</text><text x="166" y="115">Sa</text></g>
  </svg>
  <p class="lorem" style="left:17px;top:209px;width:180px">Lorem ipsum dolor sit amet, consectetur adipiscing elit. Cras vitae, blandit tortor gravida pharetra nunc. Non turpis imperdiet viverra sed vulputate nisl scelerisque donec.</p>
  <div class="heading" style="left:15px;top:245px">On Going Challenge</div>
  <div class="stats-card">
    <div class="sc-label" style="left:5px"><svg><use href="#i-run"/></svg>Distance Total</div>
    <div class="sc-value" style="left:7px">400 km</div>
    <div class="sc-label" style="left:72px"><svg><use href="#i-clock"/></svg>Average Speed</div>
    <div class="sc-value" style="left:73px">8k hours</div>
    <div class="sc-label" style="left:141px"><svg><use href="#i-flame"/></svg>Fastest Km</div>
    <div class="sc-value" style="left:142px">12.5 km/hr</div>
  </div>
  <p class="lorem" style="left:17px;top:347px;width:180px">Lorem ipsum dolor sit amet, consectetur adipiscing elit. Cras vitae, blandit tortor gravida pharetra nunc. Non turpis imperdiet viverra sed vulputate nisl scelerisque donec.</p>
  <div class="btn" style="left:16px;top:387px;width:183px;height:31px">Result</div>
  <nav class="tabbar">
    <svg class="tab-1"><use href="#i-home"/></svg>
    <svg class="tab-2"><use href="#i-run"/></svg>
    <svg class="tab-3 active"><use href="#i-chart"/></svg>
    <svg class="tab-4"><use href="#i-user"/></svg>
  </nav>
</section>

<section class="screen profile">
  <div class="status-time">9:41</div>
  <svg class="status-icons"><use href="#i-status"/></svg>
  <div class="brand brand-small">Pacebound</div>
  <div class="person">Maren Holloway</div>
  <div class="place">California, USA</div>
  <div class="avatar" role="img" aria-label="Profile photo of the runner"></div>
  <p class="lorem" style="left:13px;top:92px;width:152px">Lorem ipsum dolor sit amet, consectetur adipiscing elit. Cras vitae, blandit tortor gravida pharetra nunc. Non turpis imperdiet viverra sed vulputate nisl scelerisque donec.</p>
  <div class="heading" style="left:20px;top:139px">Prize</div>
  <div class="prize-box"><svg><use href="#i-crown"/></svg><span>FirstPrize</span></div>
  <p class="lorem" style="left:88px;top:163px;width:108px">Lorem ipsum dolor sit amet, consectetur adipiscing elit. Cras vitae, blandit tortor gravida pharetra nunc. Non turpis imperdiet viverra sed vulputate nisl scelerisque donec.</p>
  <div class="heading" style="left:18px;top:241px">Here to Win</div>
  <div class="win-card">
    <div class="win-title">Total Km</div>
    <div class="legend" style="top:27px"><i style="background:var(--orange-red)"></i>Average Speed</div>
    <div class="legend" style="top:40px"><i style="background:var(--yellow)"></i>Fastest Km</div>
    <div class="mini-ring" style="left:80px;top:24px">
      <svg viewBox="0 0 26 26" width="26" height="26"><circle cx="13" cy="13" r="11" fill="none" stroke="#d9d9d9" stroke-width="2"/><circle cx="13" cy="13" r="11" fill="none" stroke="#f26a3a" stroke-width="2.4" stroke-dasharray="55 14" transform="rotate(-90 13 13)"/></svg>
      <span>80%</span>
    </div>
    <div class="mini-ring" style="left:123px;top:24px">
      <svg viewBox="0 0 26 26" width="26" height="26"><circle cx="13" cy="13" r="11" fill="none" stroke="#d9d9d9" stroke-width="2"/><circle cx="13" cy="13" r="11" fill="none" stroke="#f6b43a" stroke-width="2.4" stroke-dasharray="48 21" transform="rotate(-180 13 13)"/></svg>
      <span>Km/hr</span>
    </div>
  </div>
  <p class="lorem" style="left:17px;top:347px;width:180px">Lorem ipsum dolor sit amet, consectetur adipiscing elit. Cras vitae, blandit tortor gravida pharetra nunc. Non turpis imperdiet viverra sed vulputate nisl scelerisque donec.</p>
  <div class="btn" style="left:16px;top:387px;width:183px;height:31px">Km countdown Join</div>
  <nav class="tabbar">
    <svg class="tab-1"><use href="#i-home"/></svg>
    <svg class="tab-2"><use href="#i-run"/></svg>
    <svg class="tab-3"><use href="#i-chart"/></svg>
    <svg class="tab-4 active"><use href="#i-user"/></svg>
  </nav>
</section>
</body>
</html>
```